Client Meeting and installation Email Follow up

I would like a follow-up email template created.
Currently, we do a lot of new construction builds and meet with clients about 6-3 months before they take possession of their new house. I want a follow-up email template to be sent after the homeowner takes possession of their house that enquires if the clients are happy about their new lighting, the service they received, and their customer service representative with Harborview Lamps and Breezes. I have attached a few files of what our current marketing looks like.
Home Owners We have already met with
Residential lighting
- Alta Light, Playfair Display, Montserrat
Designer to choose colors to be used in the design.

```html
<!DOCTYPE html>
<html lang="en">
<head>
<meta charset="utf-8">
<title>Harborview Lamps and Breezes – Residential Lighting Follow Up</title>
<link rel="stylesheet" href="https://fonts.googleapis.com/css2?family=Marcellus&family=Roboto:wght@400;500;700&display=swap">
<style>
:root{
  --ink:#0b0b0b;
  --paper:#ffffff;
  --muted:#8a8a8a;
  --body:#6f6f6f;
  --blush:#fde1de;
  --blush-ink:#1d1d1d;
  --footer:#000000;
}
*{box-sizing:border-box;margin:0;padding:0}
html,body{width:1200px;height:5224px;overflow:hidden;background:var(--paper)}
.email{position:relative;width:1200px;height:5224px;background:var(--paper);font-family:"Roboto",Arial,sans-serif;color:var(--ink)}
.abs{position:absolute}
.brand{left:0;width:1200px;text-align:center;font-family:"Marcellus",Georgia,serif;color:var(--ink);line-height:1}
.brand .top{font-size:78px;letter-spacing:2px;display:block}
.brand .bottom{font-size:48px;letter-spacing:3px;display:block;margin-top:10px}
.brand--header{top:26px}
.brand--footer{top:4724px;color:var(--paper)}
.hero-photo{left:0;top:212px;width:1200px;height:520px;background:linear-gradient(120deg,#cfc7bc 0%,#e9e4dc 40%,#8f8880 75%,#5d5853 100%)}
.intro-card{left:72px;top:636px;width:1056px;height:760px;background:var(--paper)}
.title{left:0;width:1200px;text-align:center;font-family:"Marcellus",Georgia,serif;color:var(--ink);line-height:1}
.title--l1{top:762px;font-size:78px;letter-spacing:2px}
.title--l2{top:848px;font-size:68px;letter-spacing:2px}
.intro-copy{left:128px;top:966px;width:944px;text-align:center;font-size:25px;line-height:54px;color:var(--muted)}
.offer{left:0;top:1400px;width:1200px;text-align:center;font-weight:700;font-size:92px;line-height:1}
.code{left:0;top:1512px;width:1200px;text-align:center;font-weight:700;font-size:32px}
.code span{text-decoration:underline}
.room-photo{top:1600px;width:520px;height:728px}
.room-photo--left{left:72px;background:linear-gradient(160deg,#b7a898 0%,#6f5a48 45%,#d8cdbf 100%)}
.room-photo--right{left:608px;background:linear-gradient(200deg,#3c2a1e 0%,#a98568 40%,#ece6dd 100%)}
.btn{left:424px;width:352px;height:120px;border-radius:60px;background:var(--paper);display:flex;align-items:center;justify-content:center;font-weight:500;font-size:31px;color:var(--ink);letter-spacing:.5px}
.btn--rooms{top:1904px}
.btn--banner{top:4540px}
.step-num{width:176px;height:176px;border-radius:50%;background:var(--blush);display:flex;align-items:center;justify-content:center;font-weight:700;font-size:66px;color:var(--blush-ink)}
.step-title{font-weight:700;font-size:40px;line-height:1}
.step-copy{font-size:24px;line-height:38.5px;color:var(--body);text-align:justify}
.banner-photo{left:0;top:3868px;width:1200px;height:796px;background:linear-gradient(180deg,#d9cfcd 0%,#e8dcd8 45%,#d9c6c2 100%)}
.banner-title{left:0;width:1200px;text-align:center;font-family:"Marcellus",Georgia,serif;line-height:1;color:var(--ink)}
.banner-title--l1{top:4324px;font-size:80px;letter-spacing:2px}
.banner-title--l2{top:4416px;font-size:74px;letter-spacing:2px}
.footer{left:0;top:4664px;width:1200px;height:560px;background:var(--footer)}
.legal{left:0;top:5036px;width:1200px;text-align:center;font-size:23px;color:var(--paper)}
.social{left:458px;top:5116px}
</style>
</head>
<body>
<main class="email">
  <div class="abs brand brand--header"><span class="top">HARBORVIEW</span><span class="bottom">LAMPS &amp; BREEZES</span></div>

  <div class="abs hero-photo" role="img" aria-label="Modern living room with ring pendant lights and floor-to-ceiling windows"></div>
  <div class="abs intro-card"></div>
  <h1 class="abs title title--l1">RESIDENTIAL LIGHTING</h1>
  <div class="abs title title--l2">AND INSTALLATION</div>
  <p class="abs intro-copy">Sed ut perspiciatis unde omnis iste natus error sit voluptatem accusantium doloremque laudantium, totam rem aperiam, eaque ipsa quae ab illo inventore veritatis et quasi architecto beatae vitae dicta sunt explicabo. Nemo enim ipsam voluptatem quia voluptas sit aspernatur aut odit aut fugit, sed quia consequuntur magni dolores eos qui ratione voluptatem sequi nesciunt. Neque porro quisquam est, qui dolorem ipsum quia dolor sit amet, consectetur, adipisci velit, sed quia non numquam eius modi tempora incidunt ut labore et dolore magnam aliquam quaerat voluptatem.</p>

  <div class="abs offer">100% OFF</div>
  <div class="abs code">Use Code : <span>ILIGHTS</span></div>

  <div class="abs room-photo room-photo--left" role="img" aria-label="Living room with wood slat wall, track lighting and lounge chair"></div>
  <div class="abs room-photo room-photo--right" role="img" aria-label="Bright living space with wood slat panels and potted plant"></div>
  <div class="abs btn btn--rooms">SHOP NOW</div>

  <div class="abs step-num" style="left:84px;top:2432px">01</div>
  <h2 class="abs step-title" style="left:300px;top:2434px">Lighting Experience</h2>
  <p class="abs step-copy" style="left:300px;top:2496px;width:812px">Sed ut perspiciatis unde omnis iste natus error sit voluptatem accusantium doloremque laudantium, totam rem aperiam, eaque ipsa quae ab illo inventore veritatis et quasi architecto beatae vitae dicta sunt explicabo. Nemo enim ipsam voluptatem quia voluptas sit aspernatur aut odit aut fugit, sed quia consequuntur magni dolores eos qui ratione voluptatem sequi nesciunt.</p>

  <h2 class="abs step-title" style="left:84px;top:2922px">Service Quality</h2>
  <p class="abs step-copy" style="left:84px;top:2984px;width:812px">Sed ut perspiciatis unde omnis iste natus error sit voluptatem accusantium doloremque laudantium, totam rem aperiam, eaque ipsa quae ab illo inventore veritatis et quasi architecto beatae vitae dicta sunt explicabo. Nemo enim ipsam voluptatem quia voluptas sit aspernatur aut odit aut fugit, sed quia consequuntur magni dolores eos qui ratione voluptatem sequi nesciunt.</p>
  <div class="abs step-num" style="left:940px;top:2916px">02</div>

  <div class="abs step-num" style="left:84px;top:3404px">03</div>
  <h2 class="abs step-title" style="left:300px;top:3406px">Customer Service Representative</h2>
  <p class="abs step-copy" style="left:300px;top:3468px;width:812px">Sed ut perspiciatis unde omnis iste natus error sit voluptatem accusantium doloremque laudantium, totam rem aperiam, eaque ipsa quae ab illo inventore veritatis et quasi architecto beatae vitae dicta sunt explicabo. Nemo enim ipsam voluptatem quia voluptas sit aspernatur aut odit aut fugit, sed quia consequuntur magni dolores eos qui ratione voluptatem sequi nesciunt.</p>

  <div class="abs banner-photo" role="img" aria-label="Cluster of copper, glass and white pendant lamps against a soft blush wall"></div>
  <div class="abs banner-title banner-title--l1">FALL IN LOVE</div>
  <div class="abs banner-title banner-title--l2">WITH YOUR HOME</div>
  <div class="abs btn btn--banner">SHOP NOW</div>

  <footer class="abs footer"></footer>
  <div class="abs brand brand--footer"><span class="top">HARBORVIEW</span><span class="bottom">LAMPS &amp; BREEZES</span></div>
  <p class="abs legal">© 2024&nbsp; Harborview Lamps and Breezes,All rights Reserved &nbsp;|&nbsp; Privacy Policy &nbsp;|&nbsp; Terms of Use</p>
  <svg class="abs social" width="284" height="52" viewBox="0 0 284 52" role="img" aria-label="Social media links">
    <g fill="none" stroke="#ffffff" stroke-width="3">
      <circle cx="26" cy="26" r="22"/>
      <circle cx="84" cy="26" r="22"/>
      <circle cx="142" cy="26" r="22"/>
      <circle cx="200" cy="26" r="22"/>
      <circle cx="258" cy="26" r="22"/>
    </g>
  </svg>
</main>
</body>
</html>
```